Kestrel Hill Historic District Banner

Our Historic district is located in Allentown Pennsylvania, USA and is in need of a new banner design. The banners measure 18" wide by 36" tall. The banners are hung upon decorative street lights approximately 7' above ground. The district is adjacent to a downtown area that is experiencing significant growth and economic revitalization. The district is in need of a banner that respects the historic nature of the neighborhood while also saying that this is a hip urban residential neighborhood. You can visit our website at www.kestrelhill.org to learn more about our district. I also will upload our current logo which we like but think it may need some freshening up. I will also upload an image of one of the light poles.

just added a sketch of one thought that came up during one of my board meetings. We like the idea of keeping it simple, bold, easy to digest. we just upgraded many of our street signs in a black and white theme. thought it could be used in a playful positive and negative fashion. we also have previously liked color combinations of gold and blue - gold and black - gold and sepia - parchment and sepia

```html
<!DOCTYPE html>
<html lang="en">
<head>
<meta charset="utf-8">
<title>Kestrel Hill Historic District Banner</title>
<link href="https://fonts.googleapis.com/css2?family=Cinzel:wght@500;700&family=IM+Fell+English:ital@1&display=swap" rel="stylesheet">
<style>
  :root {
    --backdrop: #eceae6;
    --parchment-light: #e6cf95;
    --parchment-deep: #d4b46c;
    --stripe-white: #ffffff;
    --stripe-gold: #d9b865;
    --sepia-ink: #3b3128;
    --emblem-tone: #8a7450;
  }
  html, body {
    margin: 0;
    width: 897px;
    height: 1200px;
    overflow: hidden;
    background: var(--backdrop);
  }
  .canvas {
    width: 897px;
    height: 1200px;
    display: flex;
    align-items: center;
    justify-content: center;
  }
  .banner {
    width: 550px;
    height: 1113px;
    display: block;
    box-shadow: 0 2px 10px rgba(0,0,0,0.12);
  }
  .wordmark {
    font-family: "Cinzel", serif;
    font-weight: 500;
    fill: var(--sepia-ink);
  }
  .tagline {
    font-family: "IM Fell English", serif;
    font-style: italic;
    fill: var(--sepia-ink);
  }
</style>
</head>
<body>
<main class="canvas">
  <svg class="banner" viewBox="0 0 210 425" xmlns="http://www.w3.org/2000/svg">
    <defs>
      <linearGradient id="parchment" x1="0" y1="0" x2="1" y2="1">
        <stop offset="0" stop-color="var(--parchment-light)"/>
        <stop offset="1" stop-color="var(--parchment-deep)"/>
      </linearGradient>
      <clipPath id="banner-edge">
        <rect width="210" height="425"/>
      </clipPath>
    </defs>

    <g clip-path="url(#banner-edge)">
      <rect class="banner-field" width="210" height="425" fill="url(#parchment)"/>

      <!-- upper-left diagonal bands -->
      <g class="corner-bands corner-bands--upper">
        <polygon points="-300,-10 35,-10 -276,435 -610,435" fill="var(--stripe-white)"/>
        <polygon points="35,-10 57,-10 -254,435 -276,435" fill="var(--stripe-gold)"/>
        <polygon points="57,-10 69,-10 -242,435 -254,435" fill="var(--stripe-white)"/>
      </g>

      <!-- lower-right diagonal bands -->
      <g class="corner-bands corner-bands--lower">
        <polygon points="454,-10 469,-10 158,435 143,435" fill="var(--stripe-white)"/>
        <polygon points="469,-10 494,-10 183,435 158,435" fill="var(--stripe-gold)"/>
        <polygon points="494,-10 800,-10 500,435 183,435" fill="var(--stripe-white)"/>
      </g>

      <rect class="district-emblem" x="44" y="78" width="72" height="92" fill="var(--emblem-tone)" opacity="0.35"
            role="img" aria-label="District emblem: line drawing of a turreted historic townhouse"/>

      <g class="title-block" transform="translate(105 292) rotate(-55)">
        <text class="wordmark" x="-78" y="-6" font-size="28">KESTREL</text>
        <text class="wordmark" x="-40" y="26" font-size="28">HILL</text>
        <line class="title-rule" x1="30" y1="16" x2="150" y2="16" stroke="var(--sepia-ink)" stroke-width="1.2"/>
        <circle cx="30" cy="16" r="1.6" fill="var(--sepia-ink)"/>
        <text class="tagline" x="-36" y="48" font-size="11">Historic District</text>
      </g>
    </g>
  </svg>
</main>
</body>
</html>
```